Lets get creative with Pelloway Finance Brochure

I have used artfolkhub before for a previous brochure which is attached business BRAMLE Automotive. I would like to work together on a new project PELLOWAY Finance. https://pellowayfinance.com.au/
It is a boutique Finance company ideally targeting the small to Medium business s along with consumer finance. I have attached previous brochure to give an idea of layout. Once we have a layout i will send wording through.

Target Market(s)

business owners

Industry/Entity Type

Finance

Font styles to use
Serif

Colors
0355a3
fef3ec

```html
<!DOCTYPE html>
<html lang="en">
<head>
<meta charset="utf-8">
<title>Pelloway Finance Tri-fold Brochure</title>
<link rel="stylesheet" href="https://fonts.googleapis.com/css2?family=Montserrat:wght@400;500;600;700;800&display=swap">
<style>
:root{
  --navy:#1f3274;
  --navy-deep:#1a2b66;
  --grey:#9a9a9c;
  --grey-light:#dcdcde;
  --text:#2a2f45;
  --muted:#7f8596;
  --page:#ffffff;
  --canvas:#ececec;
}
*{box-sizing:border-box;margin:0;padding:0}
html,body{width:686px;height:1200px;overflow:hidden;background:var(--canvas)}
body{font-family:"Montserrat",sans-serif;color:var(--text);position:relative}
.spread{position:absolute;left:20px;width:646px;height:500px;background:var(--page);box-shadow:0 3px 8px rgba(0,0,0,.18);overflow:hidden}
.spread--outer{top:60px}
.spread--inner{top:640px}
.spread-art{position:absolute;inset:0;width:646px;height:500px}
.block{position:absolute}
.heading{font-weight:700;color:var(--navy);font-size:12px;letter-spacing:.3px;text-transform:uppercase}
.body-copy{font-size:5.6px;line-height:1.42;color:var(--text);text-align:justify;margin-top:8px}
.body-copy + .body-copy{margin-top:6px}
.ticks{list-style:none;margin-top:8px}
.ticks li{position:relative;padding-left:11px;font-size:5.6px;line-height:1.4;margin-bottom:7px;text-align:justify}
.ticks li::before{content:"";position:absolute;left:0;top:1px;width:5px;height:5px;border:1px solid var(--navy);border-radius:50%}
.ticks li::after{content:"";position:absolute;left:2px;top:2.4px;width:2px;height:1.4px;border-left:1px solid var(--navy);border-bottom:1px solid var(--navy);transform:rotate(-45deg)}
.brand{text-align:center;color:var(--navy);font-weight:500}
.brand-name{display:block;font-size:17px;letter-spacing:4px}
.brand-sub{display:block;font-size:6px;letter-spacing:7px;margin-top:3px}
.brand--large .brand-name{font-size:21px;letter-spacing:5px}
.brand--large .brand-sub{font-size:7px;letter-spacing:9px}
.map-box{position:absolute;left:254px;top:118px;width:141px;height:96px;border:1.5px solid #a8a8ab;border-radius:6px;background:#f4f4f5;display:flex;align-items:center;justify-content:center;color:#d2d2d5;font-size:13px;letter-spacing:1px}
.call-label{font-size:13px;color:var(--text);text-align:center;letter-spacing:.5px}
.call-number{font-size:24px;color:var(--navy);font-weight:500;text-align:center;letter-spacing:1px;margin-top:2px}
.contact{position:absolute;left:218px;width:214px;text-align:center;font-size:7px;font-weight:600;color:var(--text)}
.contact-icon{width:30px;height:30px;margin:0 auto 5px;display:block}
.tagline{text-align:center;color:var(--muted);font-size:10px;line-height:1.3;font-weight:500}
.tagline strong{display:block;color:var(--navy);font-weight:800;font-size:13px}
.tagline small{display:block;color:var(--text);font-size:7px;margin-top:5px}
.url{text-align:center;font-size:7px;font-weight:600;color:var(--text)}
.narrow-copy{font-size:5.6px;line-height:1.4;text-align:justify}
</style>
</head>
<body>

<!-- OUTER SPREAD -->
<section class="spread spread--outer">
  <svg class="spread-art" viewBox="0 0 646 500" aria-hidden="false">
    <defs>
      <linearGradient id="mriTone" x1="0" y1="0" x2="1" y2="1">
        <stop offset="0" stop-color="#f5f4ef"/><stop offset=".6" stop-color="#dfe1e2"/><stop offset="1" stop-color="#b9bec4"/>
      </linearGradient>
      <linearGradient id="houseTone" x1="0" y1="0" x2="0" y2="1">
        <stop offset="0" stop-color="#8fb8de"/><stop offset=".45" stop-color="#5f6f82"/><stop offset="1" stop-color="#2d3138"/>
      </linearGradient>
    </defs>
    <path d="M0 0H395C330 12 250 58 150 66C90 71 35 62 0 55Z" fill="var(--navy)"/>
    <path d="M0 70C45 78 110 78 170 70C250 58 300 40 340 30" fill="none" stroke="var(--grey)" stroke-width="5"/>
    <text x="50" y="40" font-family="Montserrat,sans-serif" font-size="20" letter-spacing="5" fill="#2c3f83">PELLOWAY</text>
    <path d="M0 300C110 288 225 370 240 500H0Z" fill="var(--grey)"/>
    <path d="M0 312C100 302 210 380 226 500H0Z" fill="url(#mriTone)" role="img" aria-label="Photo of a bright medical imaging room with a scanner"/>
    <path d="M505 0H646V312C560 322 462 262 457 152C454 82 476 30 505 0Z" fill="url(#houseTone)" role="img" aria-label="Photo of a modern multi-storey house with glass balconies"/>
    <path d="M493 0C463 30 440 82 444 156C450 272 556 334 646 322" fill="none" stroke="var(--navy)" stroke-width="8"/>
  </svg>

  <div class="block" style="left:22px;top:98px;width:180px">
    <h2 class="heading">About us</h2>
    <p class="body-copy">Lorem Ipsum is simply dummy text of the printing and typesetting industry. Lorem Ipsum has been the industry's standard dummy text ever since the 1500s, when an unknown printer took a galley of type and scrambled it to make a type specimen book.</p>
    <h2 class="heading" style="margin-top:14px">Why choose us?</h2>
    <ul class="ticks">
      <li>Lorem Ipsum is simply dummy text</li>
      <li>of the printing and typesetting industry. Lorem Ipsum has been the industry's standard</li>
      <li>dummy text ever since the 1500s, when an unknown</li>
      <li>printer took a galley of type and scrambled it to make a type specimen book.</li>
    </ul>
  </div>

  <div class="block brand" style="left:218px;top:70px;width:214px">
    <span class="brand-name">PELLOWAY</span>
    <span class="brand-sub">FINANCE</span>
  </div>
  <div class="map-box">MAP</div>
  <div class="block" style="left:218px;top:240px;width:214px">
    <p class="call-label">CALL US NOW</p>
    <p class="call-number">0123456789</p>
  </div>
  <div class="contact" style="top:300px">
    <svg class="contact-icon" viewBox="0 0 30 30"><circle cx="15" cy="15" r="14" fill="#fff" stroke="#8c8c90" stroke-width="1"/><path d="M15 8a4 4 0 0 0-4 4c0 3 4 7 4 7s4-4 4-7a4 4 0 0 0-4-4z" fill="none" stroke="var(--navy)" stroke-width="1.6"/><circle cx="15" cy="12" r="1.4" fill="var(--navy)"/><path d="M10 21h10" stroke="var(--navy)" stroke-width="1.6"/></svg>
    YOUR COMPANY LOCATION
  </div>
  <div class="contact" style="top:366px">
    <svg class="contact-icon" viewBox="0 0 30 30"><circle cx="15" cy="15" r="14" fill="#fff" stroke="#8c8c90" stroke-width="1"/><circle cx="15" cy="15" r="6" fill="none" stroke="var(--navy)" stroke-width="1.6"/><ellipse cx="15" cy="15" rx="2.6" ry="6" fill="none" stroke="var(--navy)" stroke-width="1.2"/><path d="M9 15h12" stroke="var(--navy)" stroke-width="1.2"/></svg>
    yourcompanywebsite
  </div>
  <div class="contact" style="top:428px">
    <svg class="contact-icon" viewBox="0 0 30 30"><circle cx="15" cy="15" r="14" fill="#fff" stroke="#8c8c90" stroke-width="1"/><rect x="9" y="11" width="12" height="8" fill="var(--navy)"/><path d="M9 11l6 5 6-5" fill="none" stroke="#fff" stroke-width="1"/></svg>
    yourcompanyemail
  </div>

  <div class="block brand brand--large" style="left:432px;top:330px;width:214px">
    <span class="brand-name">PELLOWAY</span>
    <span class="brand-sub">FINANCE</span>
  </div>
  <div class="block tagline" style="left:432px;top:388px;width:214px">
    LOREM IPSUM IS SIMPLY DUMMY
    <strong>TEXT OF THE PRINTING</strong>
    AND TYPESETTING INDUSTRY
    <small>Lorem Ipsum has been the industry's</small>
  </div>
  <p class="block url" style="left:432px;top:470px;width:214px">www.pellowayfinance.com.au</p>
</section>

<!-- INNER SPREAD -->
<section class="spread spread--inner">
  <svg class="spread-art" viewBox="0 0 646 500">
    <defs>
      <linearGradient id="siteTone" x1="0" y1="0" x2="0" y2="1">
        <stop offset="0" stop-color="#3f86c8"/><stop offset=".45" stop-color="#a9c8e0"/><stop offset=".7" stop-color="#c9a24a"/><stop offset="1" stop-color="#8c6a3c"/>
      </linearGradient>
      <linearGradient id="carTone" x1="0" y1="0" x2="1" y2="1">
        <stop offset="0" stop-color="#2a2f38"/><stop offset=".6" stop-color="#8e959e"/><stop offset="1" stop-color="#c9ccd1"/>
      </linearGradient>
      <linearGradient id="buildingTone" x1="0" y1="0" x2="1" y2="1">
        <stop offset="0" stop-color="#ffffff"/><stop offset="1" stop-color="#e3e6ea"/>
      </linearGradient>
    </defs>
    <rect x="215" y="0" width="215" height="330" fill="url(#siteTone)" role="img" aria-label="Photo of a yellow excavator on a construction site under blue sky"/>
    <path d="M430 340C520 330 600 380 646 430V500H430Z" fill="url(#buildingTone)" role="img" aria-label="Faint photo of a modern building"/>
    <path d="M215 330C320 300 450 300 540 335C590 355 620 390 646 420V500H215Z" fill="var(--grey)"/>
    <path d="M215 340C320 312 450 312 535 345C580 362 610 392 636 430V500H215Z" fill="#fff"/>
    <path d="M430 345C500 345 570 370 636 430V500H430Z" fill="url(#buildingTone)" opacity=".9"/>
    <path d="M0 500C30 420 120 345 240 318" fill="none" stroke="var(--navy)" stroke-width="12"/>
    <path d="M22 500C60 440 140 385 215 372V500Z" fill="url(#carTone)" role="img" aria-label="Photo of the front of a silver car"/>
    <path d="M22 500C60 440 140 385 215 372" fill="none" stroke="var(--grey)" stroke-width="9"/>
  </svg>

  <div class="block" style="left:20px;top:32px;width:176px">
    <h2 class="heading">Servicing &amp; Repairs</h2>
    <p class="body-copy">Lorem Ipsum is simply dummy text of the printing and typesetting industry. Lorem Ipsum has been the industry's standard dummy text ever since the 1500s, when an unknown printer took a galley of type and scrambled it to make a type specimen book.</p>
    <p class="body-copy">Lorem Ipsum is simply dummy text of the printing and typesetting industry. Lorem Ipsum has been the industry's standard dummy text ever since the 1500s, when an unknown printer took a galley of type and scrambled it to make a type specimen book.</p>
    <h2 class="heading" style="margin-top:14px">Our services include</h2>
    <ul class="ticks">
      <li>Lorem Ipsum is simply dummy text</li>
      <li>of the printing and typesetting industry. Lorem Ipsum has been the industry's standard</li>
      <li>dummy text ever since the 1500s, when an unknown</li>
      <li>printer took a galley of type and scrambled it to make a type specimen book.</li>
      <li>Lorem Ipsum is simply dummy text</li>
      <li>of the printing and typesetting industry. Lorem Ipsum has been the industry's standard</li>
    </ul>
  </div>

  <div class="block" style="left:452px;top:32px;width:174px">
    <h2 class="heading">Lorem Ipsum</h2>
    <p class="body-copy">Lorem Ipsum is simply dummy text of the printing and typesetting industry. Lorem Ipsum has been the industry's standard dummy text ever since the 1500s, when an unknown printer took a galley of type and scrambled it to make a type specimen book.</p>
    <p class="body-copy">Lorem Ipsum is simply dummy text of the printing and typesetting industry. Lorem Ipsum has been the industry's standard dummy text ever since the 1500s, when an unknown printer took a galley of type and scrambled it to make a type specimen book.</p>
    <h2 class="heading" style="margin-top:14px">Lorem Ipsum</h2>
    <p class="body-copy">Lorem Ipsum is simply dummy text of the printing and typesetting industry. Lorem Ipsum has been the industry's standard dummy text ever since the 1500s, when an unknown printer took a galley of type and scrambled it to make a type specimen book.</p>
    <p class="body-copy">Lorem Ipsum is simply dummy text of the printing and typesetting industry. Lorem Ipsum has been the industry's standard dummy text ever since the 1500s, when an unknown printer took a galley of type and scrambled it to make a type specimen book.</p>
    <p class="body-copy">Lorem Ipsum is simply dummy text of the printing and typesetting industry. Lorem Ipsum has been the industry's standard dummy text ever since the 1500s, when an unknown printer took a galley of type and scrambled it to make a type specimen book.</p>
  </div>

  <div class="block" style="left:238px;top:374px;width:176px">
    <h2 class="heading">Lorem Ipsum</h2>
    <p class="body-copy">Lorem Ipsum is simply dummy text of the printing and typesetting industry. Lorem Ipsum has been the industry's standard dummy text ever since the 1500s, when an unknown printer took a galley of type and scrambled it to make a type specimen book.</p>
    <p class="body-copy">Lorem Ipsum is simply dummy text of the printing and typesetting industry. Lorem Ipsum has been the industry's standard dummy text ever since the 1500s,</p>
  </div>
  <p class="block narrow-copy" style="left:445px;top:405px;width:62px">Lorem Ipsum is simply dummy text of the printing and typesetting industry. Lorem Ipsum has been the industry's standard dummy text ever since the 1500s.</p>
</section>

</body>
</html>
```